Brovanix Stationery Design Project

We need a stationery design for our new business Brovanix which deals in Precision Wash Systems such as Ultrasonic cleaning and high pressure cleaning machinery.

Our colour scheme is as per the included files.

We require business cards, letterheads, a brochure folder and email signatures design
Updates

Apologies for the delay in making a decision on this project. We will be making a final decision during the course of next week

Target Market(s)

Industries ranging from medical, automotive, mining, engineering all requiring specialised cleaning services

Industry/Entity Type

Pressure Cleaning

Requirements
Must have
• Please include our supplied logo and colour scheme. The design needs to be professional but creative.

```html
<!DOCTYPE html>
<html lang="en">
<head>
<meta charset="utf-8">
<title>Brovanix Stationery</title>
<link href="https://fonts.googleapis.com/css2?family=Open+Sans:wght@400;600;700&family=Great+Vibes&display=swap" rel="stylesheet">
<style>
:root{
  --bg:#e4e5e7;
  --paper:#ffffff;
  --brand-blue:#3b4fa3;
  --ink:#5a5d62;
  --ink-soft:#9a9ca0;
  --shadow:rgba(0,0,0,.12);
}
*{box-sizing:border-box;margin:0;padding:0}
html,body{width:1200px;height:797px;overflow:hidden;background:var(--bg);font-family:"Open Sans",sans-serif;color:var(--ink)}
.sheet{position:absolute;background:var(--paper);box-shadow:0 2px 8px var(--shadow)}
.brand{display:flex;align-items:center;gap:7px}
.brand-mark{width:10px;height:10px;border-radius:50%;background:var(--brand-blue);flex:none}
.brand-name{font-weight:600;color:var(--brand-blue);line-height:1}
.brand-tagline{color:var(--ink-soft);font-size:7px;margin-top:4px;letter-spacing:.3px}

/* letterhead */
.letterhead{left:60px;top:59px;width:480px;height:679px;padding:54px 48px}
.letterhead .brand-name{font-size:20px}
.letterhead .brand-tagline{font-size:8px;margin-left:17px}
.letter-body{margin-top:34px;font-size:8.4px;line-height:1.45}
.letter-greeting{font-weight:700;margin-bottom:10px}
.letter-body p{margin-bottom:10px}
.signature{margin-top:24px}
.signature-name{font-family:"Great Vibes",cursive;font-size:26px;color:var(--ink)}
.signature-role{font-weight:700;font-size:8.4px;margin-top:-4px}
.letter-footer{position:absolute;left:48px;bottom:40px;border-left:1.5px solid var(--brand-blue);padding-left:8px;font-size:7.5px;line-height:1.5;color:var(--ink-soft)}
.letter-footer b{color:var(--ink);font-weight:700;margin-right:4px}
.web strong{color:var(--brand-blue)}

/* envelope */
.envelope{left:600px;top:59px;width:540px;height:250px;padding:26px 30px}
.envelope .brand-name{font-size:16px}
.envelope .brand-tagline{margin-left:17px}
.envelope-address{font-size:7px;color:var(--ink-soft);line-height:1.5;margin-top:6px;border-left:1.5px solid var(--brand-blue);padding-left:6px}

/* cards */
.card{top:360px;width:260px;height:150px}
.card-front{left:600px;display:flex;align-items:flex-end;justify-content:flex-end;padding:18px}
.card-front .brand-name{font-size:18px}
.card-front .brand-tagline{margin-left:17px}
.card-back{left:880px;padding:16px 18px}
.card-back .brand-name{font-size:15px}
.card-back .brand-tagline{margin-left:17px}
.card-contact{margin-top:14px;border-left:1.5px solid var(--brand-blue);padding-left:7px;font-size:7px;line-height:1.5;color:var(--ink-soft)}
.card-person{font-size:11px;color:var(--ink);margin-bottom:2px}
.card-person span{font-size:7px;color:var(--ink-soft);margin-left:6px}
</style>
</head>
<body>

<section class="sheet letterhead">
  <div>
    <div class="brand"><span class="brand-mark"></span><span class="brand-name">Brovanix</span></div>
    <div class="brand-tagline">Precision Wash Systems</div>
  </div>
  <div class="letter-body">
    <div class="letter-greeting">Lorem Ipsum,</div>
    <p>Cras mattis consectetur purus sit amet fermentum. Etiam porta sem malesuada magna mollis euismod. Integer posuere erat a ante venenatis dapibus posuere velit aliquet. Cras justo odio, dapibus ac facilisis in, egestas eget quam. Aenean eu leo quam. Pellentesque ornare sem lacinia quam venenatis vestibulum.</p>
    <p>Vivamus sagittis lacus vel augue laoreet rutrum faucibus dolor auctor. Donec sed odio dui. Etiam porta sem malesuada magna mollis euismod. Morbi leo risus, porta ac consectetur ac, vestibulum at eros. Nullam id dolor id nibh ultricies vehicula ut id elit.</p>
    <p>Donec id elit non mi porta gravida at eget metus. Fusce dapibus, tellus ac cursus commodo, tortor mauris condimentum nibh, ut fermentum massa justo sit amet risus. Cras justo odio, dapibus ac facilisis in, egestas eget quam. Cum sociis natoque penatibus et magnis dis parturient montes, nascetur ridiculus mus.</p>
    <p>Cum sociis natoque penatibus et magnis dis parturient montes, nascetur ridiculus mus. Curabitur blandit tempus porttitor. Aenean lacinia bibendum nulla sed consectetur. Lorem ipsum dolor sit amet, consectetur adipiscing elit.</p>
    <p>Cras justo odio, dapibus ac facilisis in, egestas eget quam. Morbi leo risus, porta ac consectetur ac, vestibulum at eros. Duis mollis, est non commodo luctus, nisi erat porttitor ligula, eget lacinia odio sem nec elit. Integer posuere erat a ante venenatis dapibus posuere velit aliquet. Vivamus sagittis lacus vel augue laoreet rutrum faucibus dolor auctor.</p>
    <div class="signature">
      <div class="signature-name">Your Name</div>
      <div class="signature-role">Company Director</div>
    </div>
  </div>
  <div class="letter-footer">
    <div><b>T</b>(55) 5550 1234</div>
    <div><b>E</b>daniel.ortiz@brovanix.com</div>
    <div>Ribera 14, Col. Roma, Mexico DF 06700, MX.</div>
    <div class="web">www.<strong>brovanix</strong>.com</div>
  </div>
</section>

<section class="sheet envelope">
  <div class="brand"><span class="brand-mark"></span><span class="brand-name">Brovanix</span></div>
  <div class="brand-tagline">Precision Wash Systems</div>
  <div class="envelope-address">
    <div>Ribera 14, Col. Roma, Mexico DF 06700, MX.</div>
    <div class="web">www.<strong>brovanix</strong>.com</div>
  </div>
</section>

<section class="sheet card card-front">
  <div>
    <div class="brand"><span class="brand-mark"></span><span class="brand-name">Brovanix</span></div>
    <div class="brand-tagline">Precision Wash Systems</div>
  </div>
</section>

<section class="sheet card card-back">
  <div class="brand"><span class="brand-mark"></span><span class="brand-name">Brovanix</span></div>
  <div class="brand-tagline">Precision Wash Systems</div>
  <div class="card-contact">
    <div class="card-person">Daniel Ortiz<span>Manager</span></div>
    <div>T (55) 5550 1234</div>
    <div>E daniel.ortiz@brovanix.com</div>
    <div>Ribera 14, Col. Roma, Mexico DF 06700, MX.</div>
    <div class="web">www.<strong>brovanix</strong>.com</div>
  </div>
</section>

</body>
</html>
```